Corelink Line Card

I need to create a one page line card that displays the services that my company provides and the certifications we hold.
Updates
I have an updated logo that I will post as soon as I get it later today. For now you can see an example at:
The new logo is very close to this and the colors are the same.
The file that I have posted is an example of what I think is a slick format. the upload is a two page document, but I really only like the first page. What I need a little bit of marketing and then room for the content that describes our core services and certifications.
The content of the line card needs to be divided into 9 categories:
Cloud (Virtual) Computing environments
Links are to our current brochures on these items for reference.
Greetings all,
Greetings everyone!
Target Market(s)
Small to Medium sized businesses as well as government institutions. This should be a one page "firm handshake" type exposure that tells the customer they are dealing with a first class professional operation.
Industry/Entity Type
It Company
Look and feel
Each slider illustrates characteristics of the customer's brand and the style your logo design should communicate.

```html
<!DOCTYPE html>
<html lang="en">
<head>
<meta charset="utf-8">
<title>Corelink – Line Card</title>
<link href="https://fonts.googleapis.com/css2?family=Open+Sans:wght@400;700;800&display=swap" rel="stylesheet">
<style>
  :root {
    --peach: #efcb9c;
    --peach-light: #ead7c0;
    --peach-mid: #e4d2bd;
    --orange: #d98a1c;
    --orange-bar: rgba(222, 150, 60, 0.85);
    --ink: #231f1b;
    --slate: rgba(140, 125, 110, 0.55);
    --white: #ffffff;
  }
  * { margin: 0; padding: 0; box-sizing: border-box; }
  html, body { width: 845px; height: 1200px; overflow: hidden; }
  body { font-family: "Open Sans", Arial, sans-serif; color: var(--ink); }
  .card { position: relative; width: 845px; height: 1200px; background: var(--peach); overflow: hidden; }
  .backdrop { position: absolute; inset: 0; }

  .brand-square { position: absolute; left: 58px; top: 62px; width: 140px; height: 112px; background: var(--ink); border-radius: 6px; }
  .brand-name { position: absolute; left: 250px; top: 82px; font-weight: 800; font-size: 72px; line-height: 80px; letter-spacing: 3px; color: var(--ink); white-space: nowrap; }
  .tagline { position: absolute; left: 361px; top: 189px; font-size: 17px; letter-spacing: 1px; color: var(--ink); white-space: nowrap; }

  .service { position: absolute; left: 0; width: 845px; }
  .service-bar { position: absolute; left: 0; width: 425px; height: 40px; background: var(--orange-bar); }
  .service-icon { position: absolute; left: 64px; width: 64px; height: 64px; background: var(--white); border: 3px solid var(--ink); border-radius: 10px; }
  .service-icon::after { content: ""; position: absolute; left: 14px; top: 14px; width: 30px; height: 30px; background: var(--ink); }
  .service-title { position: absolute; left: 158px; font-weight: 700; font-size: 27px; color: var(--ink); white-space: nowrap; }
  .service-title.small { font-size: 19px; line-height: 24px; }
  .service-panel { position: absolute; left: 395px; width: 450px; background: var(--slate); }
  .service-text { position: absolute; left: 449px; width: 345px; font-weight: 700; font-size: 14px; line-height: 19px; color: var(--ink); }

  .footer-bar { position: absolute; left: 0; top: 1113px; width: 640px; height: 40px; background: var(--ink); }
  .footer-url { position: absolute; left: 52px; top: 1118px; font-weight: 700; font-size: 21px; color: var(--orange); }
</style>
</head>
<body>
<main class="card">
  <svg class="backdrop" width="845" height="1200" viewBox="0 0 845 1200" aria-hidden="true">
    <polygon points="0,300 300,300 500,520 500,1200 0,1200" fill="var(--peach-light)"/>
    <polygon points="0,580 255,580 255,1200 0,1200" fill="var(--peach-mid)"/>
    <polygon points="330,300 380,300 500,440 500,480" fill="#f2d8b6"/>
  </svg>

  <div class="brand-square"></div>
  <div class="brand-name">CORELINK</div>
  <div class="tagline">MANAGED IT FOR GROWING TEAMS</div>

  <section class="service" style="top:240px">
    <div class="service-panel" style="top:2px;height:90px"></div>
    <div class="service-bar" style="top:28px"></div>
    <div class="service-icon" style="top:16px"></div>
    <div class="service-title" style="top:29px">BDR</div>
    <p class="service-text" style="top:6px">Bulletproof your Data Protection with the Highest Industry Standards in an All-In-One Backup &amp; Business Continuity Solution.</p>
  </section>

  <section class="service" style="top:340px">
    <div class="service-bar" style="top:8px;height:55px"></div>
    <div class="service-icon" style="top:3px"></div>
    <div class="service-title small" style="top:11px">Cloud (Virtual)<br>Computing enviroments</div>
    <p class="service-text" style="top:4px">Eliminate expensive start-up costs and IT management overhead with enterprise level cloud solutions.</p>
  </section>

  <section class="service" style="top:420px">
    <div class="service-panel" style="top:0;height:90px"></div>
    <div class="service-bar" style="top:30px"></div>
    <div class="service-icon" style="top:13px"></div>
    <div class="service-title" style="top:30px">Cloud Office Suite</div>
    <p class="service-text" style="top:26px">The reliability of your office suite has now been enhanced with cloud features.</p>
  </section>

  <section class="service" style="top:520px">
    <div class="service-bar" style="top:12px"></div>
    <div class="service-icon" style="top:0"></div>
    <div class="service-title" style="top:10px">Outsourced IT</div>
    <p class="service-text" style="top:12px">Corelink provides customized Proactive IT monitoring and support that.</p>
  </section>

  <section class="service" style="top:600px">
    <div class="service-panel" style="top:0;height:90px"></div>
    <div class="service-bar" style="top:22px"></div>
    <div class="service-icon" style="top:12px"></div>
    <div class="service-title" style="top:22px">Network Security</div>
    <p class="service-text" style="top:21px">How secure is your network?<br>Are you at risk? It´s time to get proactive!</p>
  </section>

  <section class="service" style="top:700px">
    <div class="service-bar" style="top:12px"></div>
    <div class="service-icon" style="top:1px"></div>
    <div class="service-title" style="top:11px">Server Care</div>
    <p class="service-text" style="top:2px">Flat-Rate Managed Server Care is a complete, 24x7x365 server monitoring, remediation, maintenance and management solution.</p>
  </section>

  <section class="service" style="top:778px">
    <div class="service-panel" style="top:0;height:90px"></div>
    <div class="service-bar" style="top:27px"></div>
    <div class="service-icon" style="top:13px"></div>
    <div class="service-title" style="top:31px;font-size:23px">Desktop and user Care</div>
    <p class="service-text" style="top:18px">Proactive Maintenance and Security Updates for your Workstations, Remote and On-Site IT Support for your Staff.</p>
  </section>

  <section class="service" style="top:870px">
    <div class="service-bar" style="top:23px"></div>
    <div class="service-icon" style="top:12px"></div>
    <div class="service-title" style="top:22px">VOIP</div>
    <p class="service-text" style="top:1px">Businesses that utilize VoIP save money and gain more communication features. Make a Smart Investment with your Small Business by switching to VoIP.</p>
  </section>

  <section class="service" style="top:958px">
    <div class="service-panel" style="top:0;height:90px"></div>
    <div class="service-bar" style="top:22px"></div>
    <div class="service-icon" style="top:11px"></div>
    <div class="service-title" style="top:25px;font-size:24px">Vendor management</div>
    <p class="service-text" style="top:6px">Get better, faster support for your third-party hardware and software investments and one point of contact for all of your vendor relationships.</p>
  </section>

  <div class="footer-bar"></div>
  <div class="footer-url">www.corelinkit.com</div>
</main>
</body>
</html>
```